WebDesign | Financial Services Firm - Risk Mitigation

We are a professional services consulting firm that specializes in high net worth individuals over $25,000,000, executives C-suite and above, closely held businesses owners, family offices and highly compensated employees.

Our focus is on risk mitigation and tax efficient strategies. Our clients take their risk on themselves and have a proven track record generating wealth. Our directive is to preserve and protect the wealth they’ve already created.

Our company Harbor Crest Advisory is geared around five directives of asset protection:
1) Legal Structuring
2) Leverage & Financing
3) Risk Management - Asset Protection & Insurance, Trustee Work
4) Asset Management & Investing - Under www.tqlvalemark.com
5) Tax Efficient Strategies

Our Company Mark is a Pentagon with a key in the middle. A pentagon is the most efficient defensive structure. Each point of a pentagon is equal distance front every point . Each side provides support to another and works together, which is the key to our clients success.

Our key colors are blue, black and silver.

We ‘re located in the Pacific Northwest with bi coastal and international clients. We have fewer, higher net worth clients and provide exceptional customer service. We do not do social media.

We'll need the following pages:
-Front Landing Page.
Front page has to have link to hbportal.docuvaultix.com for logging into secure site.
- Contact & About Us Page
- Our Team Page
- Five Sides of Wealth Management
> Legal & Business Structuring
> Leverage & Financing
> Risk Management & Asset Protection.
> Asset Management and Investing - Will link to TQL (won't be turned on for a few months)
> Tax Efficient Strategies.

Industry/Entity Type

Financial Service

Coding

Coded - Design and coding required

Number of Pages Required

5+ page

Font styles to use
Sans Serif

Colors
0555a3

Requirements
Must have
• Our key colors are blue, black and silver.

-Front Landing Page.
- Contact & About Us Page
- Our Team Page
> Leverage & Financing
Nice to have
• I have attached images that have been purchased for use on the webpage. Us or not.

location page: 847 W Alder Ln, Suite 412, Maple Hollow, OR 97990
Should not have
• lots of color.

```html
<!DOCTYPE html>
<html lang="en">
<head>
<meta charset="utf-8">
<title>Harbor Crest Advisory</title>
<link rel="stylesheet" href="https://fonts.googleapis.com/css2?family=Cinzel:wght@400;600;700&family=Montserrat:wght@400;500;600;700&display=swap">
<style>
:root{
  --blue:#0555a3;
  --blue-bright:#1a73c9;
  --sky:#2aa0e6;
  --navy:#0d2a78;
  --ink:#1b1b1f;
  --text:#3d3f45;
  --muted:#6b6e75;
  --silver:#f2f4f9;
  --silver-mid:#dbe3f2;
  --line:#dfe3ec;
  --white:#ffffff;
  --serif:'Cinzel', Georgia, serif;
  --sans:'Montserrat', Arial, sans-serif;
}
*{box-sizing:border-box;margin:0;padding:0}
html,body{width:1200px;height:4376px;overflow:hidden}
body{font-family:var(--sans);color:var(--text);background:var(--white);position:relative}
a{color:inherit;text-decoration:none}
.pentagon{clip-path:polygon(50% 0,100% 38%,82% 100%,18% 100%,0 38%)}

/* top bar + nav */
.topbar{position:absolute;left:0;top:0;width:1200px;height:29px;background:var(--blue);color:var(--white);font-size:11px}
.topbar .mail{position:absolute;left:162px;top:8px;display:flex;gap:8px;align-items:center}
.topbar .phone{position:absolute;right:162px;top:8px;display:flex;gap:8px;align-items:center}
.nav{position:absolute;left:0;top:29px;width:1200px;height:59px;background:var(--white);font-size:13px;color:var(--ink)}
.nav a{position:absolute;top:22px}
.brand-tab{position:absolute;left:505px;top:29px;width:190px;height:92px;background:var(--white);border-radius:0 0 22px 22px;z-index:3;display:flex;flex-direction:column;align-items:center;justify-content:center;gap:6px}
.brand-dot{width:22px;height:22px;border-radius:50%;background:var(--blue)}
.brand-name{font-family:var(--serif);font-weight:600;color:var(--blue);font-size:15px;letter-spacing:.5px;text-align:center;line-height:1.1}

/* hero */
.hero{position:absolute;left:0;top:88px;width:1200px;height:541px;overflow:hidden}
.hero-photo{position:absolute;inset:0;background:linear-gradient(180deg,#5b6a80 0%,#3e4a5c 40%,#2c2a2a 75%,#3a2c22 100%)}
.hero-shade{position:absolute;inset:0;background:rgba(10,20,40,.35)}
.hero-copy{position:absolute;left:0;top:218px;width:1200px;text-align:center;color:var(--white)}
.hero-copy h1{font-family:var(--serif);font-weight:400;font-size:46px;line-height:54px;letter-spacing:1px}
.hero-copy h1 span{display:block;color:var(--sky);font-weight:600}
.hero-copy p{font-size:14px;line-height:21px;margin-top:12px}
.hero-edge{position:absolute;left:0;bottom:0}

/* section headings */
.sec-title{position:absolute;left:0;width:1200px;text-align:center;font-family:var(--serif);font-size:37px;color:var(--ink);letter-spacing:1px;font-weight:400}
.rule{position:absolute;display:flex;align-items:center;gap:6px}
.rule i{display:block;width:46px;height:2px;background:var(--blue)}
.rule b{display:block;width:14px;height:14px;border-radius:50%;border:2px solid var(--blue);background:var(--white)}

/* about */
.about-frame{position:absolute;left:156px;top:660px;width:410px;height:420px;background:var(--silver)}
.about-photo{position:absolute;left:162px;top:708px;width:340px;height:345px;background:linear-gradient(180deg,#3f7fe0 0%,#8aa4c4 35%,#6c5a48 70%,#3c3229 100%)}
.about-copy{position:absolute;left:612px;top:705px;width:425px}
.about-copy h2{font-family:var(--serif);font-weight:400;font-size:37px;color:var(--ink);letter-spacing:1px}
.about-copy .mini{display:flex;align-items:center;gap:6px;margin:10px 0 18px}
.about-copy .mini b{width:14px;height:14px;border-radius:50%;border:2px solid var(--blue)}
.about-copy .mini i{width:50px;height:2px;background:var(--blue)}
.about-copy p{font-size:12.5px;line-height:21px;text-align:justify;margin-bottom:12px;color:var(--text)}
.btn{display:inline-block;background:linear-gradient(180deg,var(--blue-bright),var(--blue));color:var(--white);font-size:12.5px;padding:9px 24px;border-bottom:3px solid var(--navy)}

/* services */
.services{position:absolute;left:0;top:1130px;width:1200px;height:893px;background:var(--silver)}
.services .town{position:absolute;left:0;bottom:0;width:1200px;height:330px;background:linear-gradient(180deg,rgba(242,244,249,1) 0%,#c9ccd2 45%,#a9adb4 100%)}
.card{position:absolute;width:278px;height:323px;background:var(--white);border-radius:10px;box-shadow:0 4px 18px rgba(20,40,90,.10);padding:10px}
.card-in{width:100%;height:100%;border:1px dashed var(--line);border-radius:8px;text-align:center;padding-top:28px}
.card .icon-bg{width:120px;height:116px;background:var(--silver);margin:0 auto;display:flex;align-items:center;justify-content:center;padding-top:10px}
.card h3{font-family:var(--serif);font-weight:600;font-size:16px;color:var(--ink);margin-top:22px;letter-spacing:.8px;white-space:nowrap}
.card p{font-size:12px;line-height:21px;color:var(--muted);padding:0 14px;margin-top:6px}

/* what we do */
.step{position:absolute;left:161px;width:329px;padding:0 0 0 44px;color:var(--text)}
.step h3{font-family:var(--serif);font-weight:600;font-size:20px;color:var(--ink);letter-spacing:.6px}
.step p{font-size:12.5px;line-height:21px;margin-top:6px}
.step .dot{position:absolute;left:14px;top:5px;width:16px;height:16px;border-radius:50%;border:2px solid var(--blue)}
.step.active{background:var(--blue);border-radius:6px;padding:22px 18px 22px 44px;color:var(--white)}
.step.active h3{color:var(--white)}
.step.active .dot{border-color:var(--white);top:27px}
.hex{position:absolute;clip-path:polygon(50% 0,100% 25%,100% 75%,50% 100%,0 75%,0 25%)}

/* team */
.team{position:absolute;left:0;top:2771px;width:1200px;height:697px;background:var(--silver)}
.member{position:absolute;top:2945px;width:420px;text-align:center}
.portrait-ring{width:300px;height:285px;margin:0 auto;background:var(--silver-mid);display:flex;align-items:center;justify-content:center;padding-top:20px}
.portrait{width:250px;height:240px}
.member h3{font-size:16px;font-weight:600;color:var(--ink);margin-top:28px}
.member p{font-size:11.5px;line-height:19px;margin-top:10px;color:var(--text)}
.member .btn{margin-top:22px;font-size:13px;padding:8px 24px}
.team-divider{position:absolute;left:600px;top:3250px;width:1px;height:150px;background:var(--line)}

/* contact */
.field{position:absolute;height:43px;border:1px solid var(--line);background:var(--white);display:flex;align-items:center;font-size:12px;color:var(--text)}
.field .ico{width:40px;height:100%;border-right:1px solid var(--line);display:flex;align-items:center;justify-content:center}
.field span{padding-left:14px}
.field.area{height:85px;align-items:flex-start}
.field.area .ico{height:43px}
.field.area span{padding-top:14px}
.submit{position:absolute;left:547px;top:3859px;width:107px;height:34px;background:linear-gradient(180deg,var(--blue-bright),var(--blue));color:var(--white);font-size:13px;display:flex;align-items:center;justify-content:center;border-bottom:3px solid var(--navy)}

/* footer */
.footer-edge{position:absolute;left:0;top:3965px}
.footer{position:absolute;left:0;top:4072px;width:1200px;height:304px;background:var(--navy)}
.f-col{position:absolute;top:4087px;color:var(--white);font-size:12px}
.f-col h4{font-family:var(--serif);font-weight:600;font-size:16px;letter-spacing:1px;margin-bottom:14px}
.f-col li{list-style:none;margin-bottom:10px;line-height:15px;padding-left:14px;position:relative}
.f-col li::before{content:"›";position:absolute;left:0}
.f-brand{position:absolute;left:150px;top:4140px;width:180px;text-align:center;color:var(--white)}
.f-brand .brand-dot{background:var(--white);margin:0 auto 12px;width:26px;height:26px}
.f-brand .brand-name{color:var(--white);font-size:18px}
.f-sep{position:absolute;top:4100px;width:1px;height:190px;background:rgba(255,255,255,.25)}
.c-row{display:flex;gap:12px;margin-bottom:14px;line-height:16px}
.c-ico{width:24px;height:24px;border:1px solid rgba(255,255,255,.8);border-radius:50%;flex:none;display:flex;align-items:center;justify-content:center}
.nl-input{width:236px;height:34px;background:#3b548f;margin-top:14px;padding:10px 16px;font-size:11px}
.nl-btn{display:inline-block;margin-top:8px;background:linear-gradient(180deg,var(--blue-bright),var(--blue));padding:7px 26px;font-size:11px}
.f-bottom{position:absolute;left:162px;top:4327px;width:876px;height:1px;background:rgba(255,255,255,.25)}
.copyright{position:absolute;left:162px;top:4350px;color:var(--white);font-size:12px}
.social{position:absolute;top:4343px;width:30px;height:30px;border-radius:50%;border:1.5px solid var(--white)}
</style>
</head>
<body>

<header>
  <div class="topbar">
    <div class="mail">
      <svg width="14" height="11" viewBox="0 0 14 11" fill="none" stroke="#fff" stroke-width="1.2"><rect x=".6" y=".6" width="12.8" height="9.8"/><path d="M1 1l6 5 6-5"/></svg>
      info@harborcrestadvisory.com
    </div>
    <div class="phone">
      <svg width="13" height="13" viewBox="0 0 13 13" fill="none" stroke="#fff" stroke-width="1.2"><path d="M2 7V6a4.5 4.5 0 019 0v1"/><rect x="1" y="7" width="2.5" height="4" rx="1"/><rect x="9.5" y="7" width="2.5" height="4" rx="1"/></svg>
      1234 567 890
    </div>
  </div>
  <nav class="nav">
    <a style="left:163px">Home</a>
    <a style="left:287px">About Us</a>
    <a style="left:430px">Our Team</a>
    <a style="left:711px">Five Sides of Wealth Management</a>
    <a style="left:970px">Contact Us</a>
  </nav>
  <div class="brand-tab">
    <div class="brand-dot"></div>
    <div class="brand-name">Harbor Crest<br>Advisory</div>
  </div>
</header>

<section class="hero">
  <div class="hero-photo" role="img" aria-label="Evening view of a timber-framed office building with steep roofs among trees"></div>
  <div class="hero-shade"></div>
  <div class="hero-copy">
    <h1>We are a professional <span>services consulting</span></h1>
    <p>Firm That Specializes In High Net Worth Individuals Over <b>$25,000,000</b>,<br>Executives C-suite and Above, Closely Held Businesses Owners, Family Offices<br>and Highly Compensated Employees.</p>
  </div>
  <svg class="hero-edge" width="1200" height="120" viewBox="0 0 1200 120">
    <polygon points="0,40 600,100 1200,40 1200,120 0,120" fill="#fff"/>
    <polygon points="0,18 600,78 1200,18 1200,42 600,120 0,42" fill="#0d2a78"/>
  </svg>
</section>

<section class="about">
  <div class="about-frame pentagon"></div>
  <div class="about-photo pentagon" style="left:190px" role="img" aria-label="Office building with stone base and timber gables under a blue sky"></div>
  <div class="about-copy">
    <h2>About Us</h2>
    <div class="mini"><b></b><i></i></div>
    <p>Our focus is on risk mitigation and tax efficient strategies. Our clients take their risk on themselves and have a proven track record generating wealth. Our directive is to preserve and protect the wealth they have already created.</p>
    <p>Lorem Ipsum is simply dummy text of the printing and typesetting industry. Lorem Ipsum has been the industry's standard dummy text ever since the book.</p>
    <p>It has survived not only five centuries, but also the leap into electronic typesetting, remaining essentially unchanged.</p>
    <a class="btn">Read More</a>
  </div>
</section>

<section class="services">
  <div class="town" role="img" aria-label="Faded grey street scene of a small town with shopfronts"></div>
</section>
<h2 class="sec-title" style="top:1192px">Our Services</h2>
<div class="rule" style="left:537px;top:1244px"><i></i><b></b><i></i></div>

<div class="card" style="left:161px;top:1283px"><div class="card-in">
  <div class="icon-bg pentagon"><svg width="54" height="60" viewBox="0 0 54 60" fill="none" stroke="#0555a3" stroke-width="2"><rect x="8" y="6" width="38" height="48" rx="2"/><path d="M16 28h22M16 35h22M16 42h14"/><circle cx="27" cy="16" r="5"/></svg></div>
  <h3>LEGAL STRUCTURING</h3>
  <p>Lorem Ipsum is simply dummy text of the printing and typesetting industry. Lorem Ipsum has been the industry's standard dummy text.</p>
</div></div>
<div class="card" style="left:462px;top:1283px"><div class="card-in">
  <div class="icon-bg pentagon"><svg width="60" height="60" viewBox="0 0 60 60" fill="none" stroke="#0555a3" stroke-width="2"><ellipse cx="22" cy="14" rx="12" ry="4"/><path d="M10 14v8c0 2 5 4 12 4M10 22v8c0 2 5 4 12 4M10 30v8c0 2 5 4 12 4"/><circle cx="38" cy="38" r="13"/><path d="M38 31v14M42 34h-6a2 2 0 000 4h4a2 2 0 010 4h-6"/></svg></div>
  <h3>LEVERAGE &amp; FINANCING</h3>
  <p>Lorem Ipsum is simply dummy text of the printing and typesetting industry. Lorem Ipsum has been the industry's standard dummy text.</p>
</div></div>
<div class="card" style="left:762px;top:1283px"><div class="card-in">
  <div class="icon-bg pentagon"><svg width="60" height="60" viewBox="0 0 60 60" fill="none" stroke="#0555a3" stroke-width="2"><path d="M6 44l10-4h12l10 4 14-8"/><path d="M6 52l12-2h14l20-10"/><path d="M22 34V26M30 34V20M38 34V14M46 34V10"/><path d="M18 20l10-8 8 4 12-10"/></svg></div>
  <h3>RISK MANAGEMENT</h3>
  <p>Lorem Ipsum is simply dummy text of the printing and typesetting industry. Lorem Ipsum has been the industry's standard dummy text.</p>
</div></div>
<div class="card" style="left:311px;top:1629px"><div class="card-in">
  <div class="icon-bg pentagon"><svg width="60" height="60" viewBox="0 0 60 60" fill="none" stroke="#0555a3" stroke-width="2"><circle cx="30" cy="30" r="22"/><path d="M22 22c2-4 14-4 16 0l-3 4H25z"/><path d="M25 26c-6 6-6 18 5 18s11-12 5-18"/><path d="M30 30v10M33 32h-4a1.5 1.5 0 000 3h2a1.5 1.5 0 010 3h-4"/></svg></div>
  <h3>ASSET MANAGEMENT</h3>
  <p>Lorem Ipsum is simply dummy text of the printing and typesetting industry. Lorem Ipsum has been the industry's standard dummy text.</p>
</div></div>
<div class="card" style="left:612px;top:1629px"><div class="card-in">
  <div class="icon-bg pentagon"><svg width="60" height="60" viewBox="0 0 60 60" fill="none" stroke="#0555a3" stroke-width="2"><rect x="12" y="6" width="32" height="46" rx="2"/><text x="18" y="22" font-family="Montserrat, sans-serif" font-size="11" font-weight="700" fill="#0555a3" stroke="none">TAX</text><path d="M18 30h14M18 36h12M18 42h10"/><circle cx="42" cy="42" r="9"/><path d="M42 37v10"/></svg></div>
  <h3>TAX EFFICIENT STRATEGIES</h3>
  <p>Lorem Ipsum is simply dummy text of the printing and typesetting industry. Lorem Ipsum has been the industry's standard dummy text.</p>
</div></div>

<section class="what">
  <h2 class="sec-title" style="top:2089px">What We Do</h2>
  <div class="rule" style="left:537px;top:2142px"><i></i><b></b><i></i></div>
  <div class="step active" style="top:2224px"><span class="dot"></span><h3>DISCOVER</h3><p>Lorem Ipsum is simply dummy text of the printing and typesetting industry. Lorem Ipsum has been the dummy text.</p></div>
  <div class="step" style="top:2410px"><span class="dot"></span><h3>CURATE</h3><p>Lorem Ipsum is simply dummy text of the printing and typesetting industry. Lorem Ipsum has been the dummy text.</p></div>
  <div class="step" style="top:2560px"><span class="dot"></span><h3>AMPLIFY</h3><p>Lorem Ipsum is simply dummy text of the printing and typesetting industry. Lorem Ipsum has been the dummy text.</p></div>
  <div class="hex" style="left:561px;top:2307px;width:240px;height:262px;background:linear-gradient(160deg,#2a4a8c,#1c3168)" role="img" aria-label="Close-up of a steel vault door in blue tone"></div>
  <div class="hex" style="left:801px;top:2176px;width:240px;height:262px;background:linear-gradient(160deg,#6a5a8a,#b07a5a 55%,#d88a7a)" role="img" aria-label="Stacks of coins on banknotes"></div>
  <div class="hex" style="left:801px;top:2438px;width:240px;height:262px;background:linear-gradient(180deg,#4a5a9a,#3a3448 55%,#8a6a58)" role="img" aria-label="Town street at dusk with light trails"></div>
</section>

<section class="team"></section>
<h2 class="sec-title" style="top:2837px">Our Team</h2>
<div class="rule" style="left:537px;top:2889px"><i></i><b></b><i></i></div>
<div class="member" style="left:164px">
  <div class="portrait-ring pentagon"><div class="portrait pentagon" style="background:linear-gradient(180deg,#6f9a5a,#3a4a3a 60%,#2a2e36)" role="img" aria-label="Portrait of Marcus Ellery in a suit outdoors"></div></div>
  <h3>Marcus Ellery</h3>
  <p>Marcus Ellery is the Financial Strategist and Founder who partners with C-Suite Executives, Family Offices, Real Estate Investors and Closely Held Business Owners to protect and maximize their wealth.</p>
  <a class="btn">Read More</a>
</div>
<div class="member" style="left:614px">
  <div class="portrait-ring pentagon"><div class="portrait pentagon" style="background:linear-gradient(180deg,#7a6a5a,#5a4a44 50%,#5a58c8)" role="img" aria-label="Portrait of Peter Halvorsen in a cap and sunglasses"></div></div>
  <h3>Peter Halvorsen</h3>
  <p>Peter Halvorsen is the CFO and Strategist for our closely held businesses. As a former CPA, he takes in-depth roles in closely held companies as a financial consultant during times of exit or transition.</p>
  <a class="btn">Read More</a>
</div>
<div class="team-divider"></div>

<section class="contact">
  <h2 class="sec-title" style="top:3532px">Contact Us</h2>
  <div class="rule" style="left:537px;top:3584px"><i></i><b></b><i></i></div>
  <div class="field" style="left:255px;top:3626px;width:337px"><div class="ico"><svg width="14" height="14" viewBox="0 0 14 14" fill="none" stroke="#777"><circle cx="7" cy="4.5" r="3"/><path d="M1.5 13c0-3 2.5-5 5.5-5s5.5 2 5.5 5"/></svg></div><span>Your Name*</span></div>
  <div class="field" style="left:609px;top:3626px;width:336px"><div class="ico"><svg width="14" height="11" viewBox="0 0 14 11" fill="none" stroke="#777"><rect x=".5" y=".5" width="13" height="10"/><path d="M1 1l6 5 6-5"/></svg></div><span>Email*</span></div>
  <div class="field" style="left:255px;top:3686px;width:337px"><div class="ico"><svg width="14" height="14" viewBox="0 0 14 14" fill="none" stroke="#777"><path d="M2 1.5h3l1.5 3.5-2 1.2a8 8 0 003.3 3.3l1.2-2 3.5 1.5v3c-6 .5-11-4.5-10.5-10.5z"/></svg></div><span>Phone*</span></div>
  <div class="field" style="left:609px;top:3686px;width:336px"><div class="ico"><svg width="14" height="14" viewBox="0 0 14 14" fill="none" stroke="#777"><rect x=".5" y="2.5" width="11" height="11"/><path d="M6 8l6.5-6.5 1 1L7 9H6z"/></svg></div><span>Inquiry For*</span></div>
  <div class="field area" style="left:255px;top:3749px;width:690px"><div class="ico"><svg width="16" height="14" viewBox="0 0 16 14" fill="none" stroke="#777"><rect x=".5" y=".5" width="11" height="8"/><path d="M4 11h8l3 2.5V5h-3"/></svg></div><span>How can we help you?</span></div>
  <a class="submit">Submit</a>
</section>

<footer>
  <svg class="footer-edge" width="1200" height="108" viewBox="0 0 1200 108">
    <polygon points="0,108 600,20 1200,108" fill="#0d2a78"/>
    <polygon points="0,92 600,0 1200,92 1200,108 600,20 0,108" fill="#0555a3"/>
  </svg>
  <div class="footer"></div>
  <div class="f-brand">
    <div class="brand-dot"></div>
    <div class="brand-name">Harbor Crest<br>Advisory</div>
  </div>
  <div class="f-sep" style="left:335px"></div>
  <div class="f-col" style="left:358px;width:150px">
    <h4>QUICK LINKS</h4>
    <ul><li>Home</li><li>About Us</li><li>Our Team</li><li>Five Sides of Wealth Management</li><li>Contact Us</li></ul>
  </div>
  <div class="f-sep" style="left:522px"></div>
  <div class="f-col" style="left:547px;width:230px">
    <h4>CONTACT DETAIL</h4>
    <div class="c-row"><span class="c-ico"><svg width="10" height="12" viewBox="0 0 10 12" fill="none" stroke="#fff"><path d="M5 11s4-4 4-6.5a4 4 0 00-8 0C1 7 5 11 5 11z"/><circle cx="5" cy="4.5" r="1.3"/></svg></span><div><b style="font-weight:600">Harbor Crest Advisory</b><br>847 W Alder Ln, Suite 412,<br>Maple Hollow, OR 97990</div></div>
    <div class="c-row"><span class="c-ico"><svg width="11" height="11" viewBox="0 0 13 13" fill="none" stroke="#fff" stroke-width="1.2"><path d="M2 7V6a4.5 4.5 0 019 0v1"/><rect x="1" y="7" width="2.5" height="4" rx="1"/><rect x="9.5" y="7" width="2.5" height="4" rx="1"/></svg></span><div style="padding-top:4px">1234 567 890</div></div>
    <div class="c-row"><span class="c-ico"><svg width="11" height="9" viewBox="0 0 14 11" fill="none" stroke="#fff" stroke-width="1.2"><rect x=".6" y=".6" width="12.8" height="9.8"/><path d="M1 1l6 5 6-5"/></svg></span><div style="padding-top:4px">info@harborcrestadvisory.com</div></div>
  </div>
  <div class="f-sep" style="left:785px"></div>
  <div class="f-col" style="left:804px;width:240px">
    <h4>NEWSLETTER</h4>
    <div style="font-size:11px;line-height:15px">You can be always up to date with our<br>Company news</div>
    <div class="nl-input">Enter your Email*</div>
    <a class="nl-btn">Submit</a>
  </div>
  <div class="f-bottom"></div>
  <div class="copyright">Copyright 2021 Harbor Crest Advisory. All Rights Reserved.</div>
  <span class="social" style="left:932px"></span>
  <span class="social" style="left:970px"></span>
  <span class="social" style="left:1008px"></span>
</footer>

</body>
</html>
```